Photography Studio Prep Guide Design Needed

I have a prep guide I send to all parents who book a session - It is outdated and ugly. I want a gorgeous, clean, modern upscale look for the brochure I send.

I already have the text and can provide photos for the final design. I want the cover to be clean and upscale and modern, with a happy feel.

Target Market(s)

My clients for an upscale Newborn Photography Studio

Requirements
Must have
• space for my photos, an upscale clean feel
Nice to have
• I love color, but don't want the brochure to look busy. I love cream, white, pale pink.

```html
<!DOCTYPE html>
<html lang="en">
<head>
<meta charset="utf-8">
<title>Newborn Session Prep Guide</title>
<link href="https://fonts.googleapis.com/css2?family=Great+Vibes&family=Lato:wght@400;700&family=Playball&family=Roboto+Condensed:wght@300&display=swap" rel="stylesheet">
<style>
  :root {
    --plum: #7b2a56;
    --plum-deep: #6a2049;
    --plum-soft: #9c4a72;
    --white: #ffffff;
    --cream: #f6efe9;
    --ink: #4a3a42;
    --stage: #e9e4e6;
  }
  * { margin: 0; padding: 0; box-sizing: border-box; }
  html, body { width: 1200px; height: 1200px; overflow: hidden; }
  body { background: var(--stage); position: relative; font-family: "Lato", sans-serif; }

  .page { position: absolute; top: 314px; width: 536px; height: 670px; overflow: hidden; box-shadow: 0 6px 20px rgba(0,0,0,.18); }
  .page--front { left: 42px; background: linear-gradient(160deg, var(--plum-soft), var(--plum) 55%, var(--plum-deep)); }
  .page--inside { left: 622px; background: var(--white); }

  /* Front */
  .cover-photo { position: absolute; left: 0; top: 0; width: 380px; height: 670px;
    background: linear-gradient(90deg, #e8c7b4 0%, #dcb2a3 45%, rgba(180,110,140,.6) 75%, rgba(123,42,86,0) 100%),
                linear-gradient(180deg, #bcd3e0 0%, #e3bfae 30%, #d9a89a 100%); }
  .brand-mark { position: absolute; left: 366px; top: 36px; width: 140px; text-align: center; color: var(--white); }
  .brand-mark__dot { width: 46px; height: 46px; border: 1.5px solid var(--white); border-radius: 50%; margin: 0 auto 8px; }
  .brand-mark__name { font-family: "Lato", sans-serif; font-size: 12px; letter-spacing: 2px; text-transform: uppercase; }
  .cover-title { position: absolute; right: 30px; text-align: right; color: var(--white); font-family: "Roboto Condensed", sans-serif; font-weight: 300; line-height: 1; }
  .cover-title--main { top: 150px; font-size: 74px; }
  .cover-title--sub { top: 218px; font-size: 74px; opacity: .92; }
  .cover-script { position: absolute; right: 30px; top: 288px; font-family: "Playball", cursive; font-size: 56px; color: var(--white); line-height: 1; }
  .edge-tab { position: absolute; right: 0; width: 14px; background: var(--white); }
  .edge-tab--upper { top: 298px; height: 56px; }
  .edge-tab--lower { top: 594px; height: 44px; }
  .cover-circle { position: absolute; top: 404px; width: 144px; height: 144px; border-radius: 50%; border: 2px solid var(--white); padding: 6px; }
  .cover-circle__fill { width: 100%; height: 100%; border-radius: 50%; }
  .cover-circle--flowers { left: 220px; }
  .cover-circle--flowers .cover-circle__fill { background: radial-gradient(circle, #e8a07e 0%, #e2845c 45%, #e8a93a 100%); }
  .cover-circle--blanket { left: 377px; }
  .cover-circle--blanket .cover-circle__fill { background: radial-gradient(circle, #f2e6e0 0%, #f6ede8 60%, #ead7cf 100%); }
  .cover-url { position: absolute; right: 30px; top: 612px; font-size: 11px; letter-spacing: 2.2px; color: var(--white); }

  /* Inside */
  .inside-title { position: absolute; left: 0; right: 0; top: 22px; text-align: center; font-family: "Playball", cursive; font-size: 34px; line-height: 38px; color: var(--plum); }
  .inside-intro { position: absolute; left: 0; right: 0; top: 104px; text-align: center; font-size: 10.6px; line-height: 14px; color: var(--ink); }
  .nursing-photo { position: absolute; left: 8px; top: 140px; width: 196px; height: 180px; border-radius: 50%;
    background: radial-gradient(circle, #e9c8b6 0%, #2a2d3c 28%, #f1ece6 52%, rgba(255,255,255,0) 72%); }
  .section-label { position: absolute; font-family: "Great Vibes", cursive; font-size: 26px; line-height: 1; }
  .section-rule { position: absolute; height: 1px; right: 0; }
  .section-label--nursing { left: 403px; top: 176px; color: var(--plum); }
  .section-rule--nursing { left: 481px; top: 192px; background: var(--plum); }
  .nursing-text { position: absolute; left: 226px; top: 208px; width: 285px; font-size: 7.8px; line-height: 10px; color: var(--ink); text-align: justify; text-align-last: right; }
  .feeding-band { position: absolute; left: 0; right: 0; top: 325px; height: 284px; background: var(--plum); }
  .section-label--feeding { left: 126px; top: 352px; color: var(--white); }
  .section-rule--feeding { left: 216px; top: 368px; background: var(--white); }
  .feeding-text { position: absolute; left: 26px; top: 385px; width: 177px; font-size: 7.8px; line-height: 10px; color: var(--white); text-align: justify; }
  .feeding-photo { position: absolute; left: 224px; top: 379px; width: 312px; height: 231px;
    background: linear-gradient(135deg, #f3e7de 0%, #ead2c4 45%, #f6efe8 100%); }
  .inside-tab { position: absolute; left: 0; top: 622px; width: 14px; height: 36px; background: var(--plum); }
  .inside-url { position: absolute; left: 24px; top: 634px; font-size: 11px; letter-spacing: 2.2px; color: var(--plum); }
</style>
</head>
<body>
  <section class="page page--front">
    <div class="cover-photo" role="img" aria-label="Sleeping newborn in a knitted bonnet on a soft blanket"></div>
    <div class="brand-mark">
      <div class="brand-mark__dot"></div>
      <div class="brand-mark__name">Lily Rosewood</div>
    </div>
    <h1 class="cover-title cover-title--main">NEWBORN</h1>
    <div class="cover-title cover-title--sub">SESSION</div>
    <div class="cover-script">Prep Guide</div>
    <div class="edge-tab edge-tab--upper"></div>
    <div class="cover-circle cover-circle--flowers"><div class="cover-circle__fill" role="img" aria-label="Newborn wrapped in a nest of orange and pink flowers"></div></div>
    <div class="cover-circle cover-circle--blanket"><div class="cover-circle__fill" role="img" aria-label="Newborn with a flower headband asleep on a cream blanket"></div></div>
    <div class="cover-url">www.lilyrosewoodstudio.com</div>
    <div class="edge-tab edge-tab--lower"></div>
  </section>

  <section class="page page--inside">
    <h2 class="inside-title">Parent Instructions &amp;<br>Preparations</h2>
    <p class="inside-intro">Congratulations on expecting a baby!<br>Here are my instructions to ensure a successful newborn photography session.<br>Please follow these instructions as closely as possible.</p>

    <div class="nursing-photo" role="img" aria-label="Newborn curled in a navy wrap inside a white basket"></div>
    <h3 class="section-label section-label--nursing">nursing</h3>
    <div class="section-rule section-rule--nursing"></div>
    <p class="nursing-text">If you are nursing, please avoid eating anything spicy (hot sauce, hot peppers, curry, etc.) that might upset baby's tummy for 24 hours preceding your scheduled session. Please if you are breastfeeding do NOT drink caffeine or coffee before your session – I know this is hard but baby will be wired if you have caffeine. If you notice baby has a lot of gas after feedings please check with your pediatrician and bring gas drops (Tummy-Ease or other brand) to your session. The most common reason a baby will not settle for a session is gas pressure/discomfort.</p>

    <div class="feeding-band"></div>
    <h3 class="section-label section-label--feeding">feeding</h3>
    <div class="section-rule section-rule--feeding"></div>
    <p class="feeding-text">Feed the baby as much as possible in the 24 hours preceding your session – this will help minimize the amount baby needs to feed during the session, and will help baby sleep as long and as soundly as possible. Feed baby 2-3 hours before your session and not again until you arrive. This feeding is planned in your session time and it's not rushed. Please bring an extra bottle of formula or breastmilk to the session if possible – sometimes a small amount of milk in a bottle can quickly soothe a baby back to sleep without requiring a full feeding. I will respect your wishes if you choose not to use a bottle, but please understand we may have to pass on some poses if baby will not settle in position, and I cannot use a bottle to soothe them into the pose.</p>
    <div class="feeding-photo" role="img" aria-label="Sleeping newborn resting on hands beside a small striped toy bunny"></div>

    <div class="inside-tab"></div>
    <div class="inside-url">www.lilyrosewoodstudio.com</div>
  </section>
</body>
</html>
```